Napa Winery - Chardonnay wine label

We are looking for a label for a new Napa Valley winery - chardonnay wine. The winery is "Harrowgate Ridge Vintners" and we would like to see it depicted on a white wine (chardonnay style) bottle. The winery is called Harrowgate Ridge Vintners.

We are open to ideas!

Target Market(s)

High-end chardonnay lovers

Requirements
Nice to have
• Painted or etched label onto bottle

```html
<!DOCTYPE html>
<html lang="en">
<head>
<meta charset="utf-8">
<title>Harrowgate Ridge Vintners – Chardonnay Label</title>
<link rel="stylesheet" href="https://fonts.googleapis.com/css2?family=Cinzel:wght@600;700&family=Pinyon+Script&display=swap">
<style>
  :root {
    --page: #ffffff;
    --gold-light: #f6e39a;
    --gold: #cfa73f;
    --gold-deep: #8c6a1c;
    --gold-shadow: #6b4f12;
    --sky-olive: #8da62c;
    --vine-light: #93b03a;
    --vine: #6f8e24;
    --vine-mid: #557219;
    --vine-dark: #34480c;
    --cream: #f7f4ea;
    --forest: #3e4f22;
    --ink: #1d1606;
    --white: #ffffff;
  }
  * { margin: 0; padding: 0; box-sizing: border-box; }
  html, body {
    width: 1000px; height: 1200px; overflow: hidden;
    background: var(--page);
  }
  .canvas { position: relative; width: 1000px; height: 1200px; }

  .label {
    position: absolute; left: 120px; top: 195px;
    width: 760px; height: 810px;
    padding: 16px;
    background: linear-gradient(135deg, var(--gold-deep) 0%, var(--gold-light) 22%, var(--gold) 45%, var(--gold-light) 70%, var(--gold-deep) 100%);
    box-shadow: 0 10px 30px rgba(0,0,0,0.18);
  }
  .label__inner {
    position: relative; width: 100%; height: 100%;
    background: var(--cream);
  }
  .vineyard-art {
    position: absolute; left: 0; top: 0; width: 100%; height: 440px;
    background:
      radial-gradient(ellipse 22% 34% at 84% 26%, rgba(52,72,12,0.85) 0%, rgba(85,114,25,0.5) 55%, transparent 100%),
      radial-gradient(ellipse 70% 22% at 30% 20%, rgba(52,72,12,0.55) 0%, transparent 100%),
      radial-gradient(ellipse 60% 35% at 20% 95%, rgba(147,176,58,0.7) 0%, transparent 100%),
      linear-gradient(178deg,
        var(--sky-olive) 0%,
        var(--vine-mid) 14%,
        var(--vine-dark) 26%,
        var(--vine) 38%,
        var(--vine-mid) 50%,
        var(--vine-light) 62%,
        var(--vine-mid) 74%,
        var(--vine) 86%,
        var(--vine-dark) 100%);
  }
  .varietal {
    position: absolute; left: 0; top: 574px; width: 100%; height: 119px;
    display: flex; align-items: center; justify-content: center;
    font-family: "Cinzel", serif; font-weight: 700; font-size: 42px; letter-spacing: 2px;
    background: linear-gradient(180deg, var(--gold) 0%, var(--gold-deep) 100%);
    -webkit-background-clip: text; background-clip: text; color: transparent;
    padding-top: 6px;
  }
  .region-band {
    position: absolute; left: 0; bottom: 0; width: 100%; height: 83px;
    background: var(--forest);
    display: flex; align-items: center; justify-content: center; gap: 28px;
  }
  .region-band__rule { width: 70px; height: 2px; background: var(--cream); opacity: 0.85; }
  .region-band__name {
    font-family: "Pinyon Script", cursive; font-size: 40px; color: var(--white);
    line-height: 1;
  }

  .name-plaque {
    position: absolute; left: 99px; top: 646px; width: 802px; height: 140px;
  }
</style>
</head>
<body>
<div class="canvas">
  <div class="label">
    <div class="label__inner">
      <div class="vineyard-art" role="img" aria-label="Green-toned engraving of vineyard rows sweeping across rolling hills, with a hanging grape cluster and vine leaves at upper right"></div>
      <div class="varietal">CHARDONNAY</div>
      <div class="region-band">
        <span class="region-band__rule"></span>
        <span class="region-band__name">Napa Valley</span>
        <span class="region-band__rule"></span>
      </div>
    </div>
  </div>

  <svg class="name-plaque" viewBox="0 0 802 140" xmlns="http://www.w3.org/2000/svg">
    <defs>
      <linearGradient id="plaqueGold" x1="0" y1="0" x2="0" y2="1">
        <stop offset="0" stop-color="#8c6a1c"/>
        <stop offset="0.18" stop-color="#f6e39a"/>
        <stop offset="0.5" stop-color="#cfa73f"/>
        <stop offset="0.82" stop-color="#f1d97f"/>
        <stop offset="1" stop-color="#8c6a1c"/>
      </linearGradient>
      <linearGradient id="plaqueSheen" x1="0" y1="0" x2="1" y2="0">
        <stop offset="0" stop-color="#ffffff" stop-opacity="0"/>
        <stop offset="0.5" stop-color="#ffffff" stop-opacity="0.35"/>
        <stop offset="1" stop-color="#ffffff" stop-opacity="0"/>
      </linearGradient>
    </defs>
    <path class="name-plaque__edge" fill="#6b4f12"
      d="M40 2 H762 A16 16 0 0 0 778 18 Q800 70 778 122 A16 16 0 0 0 762 138 H40 A16 16 0 0 0 24 122 Q2 70 24 18 A16 16 0 0 0 40 2 Z"/>
    <path class="name-plaque__face" fill="url(#plaqueGold)"
      d="M44 8 H758 A16 16 0 0 0 772 22 Q792 70 772 118 A16 16 0 0 0 758 132 H44 A16 16 0 0 0 30 118 Q10 70 30 22 A16 16 0 0 0 44 8 Z"/>
    <rect x="60" y="14" width="682" height="40" fill="url(#plaqueSheen)"/>
    <text class="name-plaque__title" x="401" y="88" text-anchor="middle"
      font-family="Cinzel, serif" font-weight="700" font-size="44" fill="#1d1606"
      textLength="700" lengthAdjust="spacingAndGlyphs"><tspan font-size="54">H</tspan>ARROWGATE <tspan font-size="54">R</tspan>IDGE <tspan font-size="54">V</tspan>INTNERS</text>
  </svg>
</div>
</body>
</html>
```